A colorful, playful, nerdy, creative logo for a business analytics and marketing analytics company.

We need a logo and website design for a new company based in Florida called Pathways Above Numbers Guild. We provide marketing, consumer and business insights through the use of market research, business analytics and marketing analytics. We are a collection of several individuals each with specific expertise and come together to provide the best possible insights about their consumers/guests/customers. We would like to see a design that uses colors that show a free spirit but deeply rooted in analytics " a super nerd " Along those steps, we would like to see either a playful, nerdy, creative logo or one that includes the full or partial name of the company. We have simplified our "brand" by saying when you initially start with us you may have several questions "?" through the process of learning about your consumers/brand ">" incredible solutions, strategies are developed "!" So something like a ?>! symbol would be interesting. Although the name of the company sounds very complex and very long to write, we would be interested in thoughtful ways of shorting the name or incorporating into the final logo design
Updates

Target Market(s)

Business or organizations that currently do not have an analytics/research function

Industry/Entity Type

Business

Contact Information for Business Card

Incorporate final logo and colors font. In the past, I have used a "wordle" website to show 10 common research terms scattered about .. showing them as strength or core competencies.

Logo Text

?>! or Pathways Above Numbers Guild or PAN Guild

Coding

Coded - Design and coding required

Number of Pages Required

4 page

Font styles to use
Sans Serif
Decorative

Requirements
Must have
• The project must communicate analytics/scientific. It must we unique but not unique for the sack of being unique.
• It must either be a logo or a simple way to communicate the company name Pathways Above Numbers Guild
Nice to have
• Again incorporating the symbols ?>! in that order. Showing confusion to gaining insights and then developing incredible solutions that are used to effect consumer behavior.
• Look to CPG ( consumer package goods) industry to input
Should not have
• I am pretty open to suggestions.

```html
<!DOCTYPE html>
<html lang="en">
<head>
<meta charset="utf-8">
<title>Pathways Above Numbers Guild</title>
<link href="https://fonts.googleapis.com/css2?family=Montserrat:wght@400;600;700&family=Nunito+Sans:wght@400;600;700&display=swap" rel="stylesheet">
<style>
:root{
  --page-bg:#e7e7ea;
  --white:#ffffff;
  --navy:#1c1a4f;
  --navy-deep:#14123a;
  --purple:#3b387a;
  --blue:#1f7fc1;
  --ink:#2b2b3a;
  --grey:#8e8c8a;
  --band:#2b2623;
  --line:#c9c9d3;
}
*{box-sizing:border-box;margin:0;padding:0}
html,body{width:1200px;height:3448px;overflow:hidden}
body{background:var(--page-bg);font-family:"Nunito Sans",Arial,sans-serif;color:var(--ink);position:relative}
.page{position:absolute;left:18px;top:0;width:1164px;height:3430px;background:var(--white);overflow:hidden}
.abs{position:absolute}
h2,h3,h4,.nav a,.btn,.brand{font-family:"Montserrat",Arial,sans-serif}

/* header */
.header{left:0;top:0;width:1164px;height:202px;background:var(--white)}
.brand{font-weight:700;font-size:20px;color:var(--navy);display:flex;align-items:center;gap:10px}
.brand .dot{width:16px;height:16px;border-radius:50%;background:var(--blue)}
.header .brand{left:30px;top:92px}
.topbar{left:742px;top:12px;width:422px;height:34px;background:var(--navy);border-radius:17px 0 0 17px;color:var(--white);font-size:12px;display:flex;align-items:center;gap:16px;padding-left:30px}
.topbar .item{display:flex;align-items:center;gap:6px}
.social{display:flex;gap:8px;margin-left:auto;margin-right:18px}
.social i{display:block;width:12px;height:12px;background:var(--white);border-radius:2px}
.nav{left:420px;top:102px;display:flex;gap:34px}
.nav a{display:flex;align-items:center;gap:7px;font-size:12px;font-weight:600;color:var(--navy);text-decoration:none;text-transform:uppercase}
.nav a.active{color:var(--blue)}
.nav svg{width:16px;height:16px}

/* hero */
.hero{left:0;top:202px;width:1164px;height:522px;background:radial-gradient(ellipse at 60% 45%,#5fc4f0 0%,#1c6ea8 35%,#0d2c55 75%,#0a1a35 100%)}
.slider-dots{left:546px;top:488px;display:flex;gap:8px}
.slider-dots i{width:22px;height:4px;background:rgba(255,255,255,.5)}
.slider-dots i:first-child{background:var(--white)}
.intro{left:0;top:724px;width:1164px;height:180px;background:var(--band);box-shadow:0 10px 14px rgba(0,0,0,.25)}
.intro .lead{left:40px;top:40px;font-family:"Montserrat",Arial,sans-serif;font-weight:700;text-transform:uppercase}
.intro .lead .l1{font-size:20px;color:var(--white)}
.intro .lead .l2{font-size:20px;color:#8f8a86;margin-top:10px}
.intro .lead .l3{font-size:27px;color:var(--white);margin-top:6px}
.intro p{left:566px;top:40px;width:560px;font-size:16px;line-height:22px;color:#b9b4ae}

/* section titles */
.title{left:0;width:1164px;display:flex;align-items:center;justify-content:center;gap:24px;font-size:22px;font-weight:700;text-transform:uppercase}
.title::before,.title::after{content:"";width:70px;height:1px;background:currentColor;opacity:.6}
.title .acc{color:var(--blue)}
.btn{position:absolute;height:42px;border:2px solid var(--navy);border-radius:8px;display:flex;align-items:center;justify-content:center;font-size:15px;font-weight:600;letter-spacing:1px;text-transform:uppercase}

/* who */
.who .title{top:958px;color:var(--navy)}
.who p{position:absolute;left:60px;width:1044px;text-align:center;font-size:14px;line-height:20px;color:#4a4a55}
.who .btn{left:430px;top:1166px;width:304px;color:var(--navy);border-color:var(--navy)}

/* what */
.what{left:0;top:1265px;width:1164px;height:639px;background:linear-gradient(135deg,#4b4a85 0%,#3a377a 50%,#2f2c6c 100%)}
.what .title{top:52px;color:var(--white)}
.what .sub{top:122px;left:0;width:1164px;text-align:center;color:var(--white);font-size:15px;font-weight:700}
.ring{left:0;top:0}
.svc{width:242px;height:242px;border-radius:50%;background:var(--white);display:flex;flex-direction:column;align-items:center;padding-top:30px;text-align:center}
.svc svg{width:54px;height:54px}
.svc p{width:180px;margin-top:12px;font-size:14px;line-height:18px;color:#3f3f4c}
.what .btn{left:430px;top:540px;width:304px;color:var(--white);border-color:var(--white)}

/* expertise */
.expertise{left:0;top:1904px;width:1164px;height:511px;background:linear-gradient(90deg,#d9dde3 0%,#f2f3f5 45%,#e4e7ec 100%)}
.expertise .title{top:50px;color:var(--navy)}
.exp-text{width:236px;font-size:13px;line-height:17px;color:#4a4a55}
.exp-text h4{font-size:13px;font-weight:700;color:var(--navy);text-transform:uppercase;margin-bottom:2px}
.core .brand{color:var(--white);font-size:22px;position:absolute;left:503px;top:2303px;width:200px;justify-content:center}

/* news */
.news{left:0;top:2415px;width:1164px;height:556px;background:linear-gradient(135deg,#2e2b6b 0%,#232055 60%,#1c1a4a 100%)}
.news .title{top:52px;color:var(--white)}
.card{width:322px;color:var(--white)}
.card .photo{height:189px;border:4px solid var(--white);border-radius:8px}
.card h4{margin-top:20px;font-size:15px;font-weight:600;line-height:20px;text-transform:uppercase}
.card p{margin-top:14px;font-size:14px;line-height:18px;color:#e6e5f2}

/* footer */
.foot-tab{left:454px;top:2935px;width:256px;height:60px;background:var(--white);border-radius:36px 36px 0 0}
.footer .brand{left:0;width:1164px;top:3010px;justify-content:center}
.col{top:3150px}
.col h4{font-size:14px;font-weight:700;color:var(--ink);text-transform:uppercase;padding-bottom:8px;border-bottom:1px solid var(--line);width:224px;margin-bottom:14px}
.col li{list-style:none;font-size:13px;line-height:20px;color:var(--ink)}
.contact-row{display:flex;gap:12px;align-items:flex-start;font-size:12px;line-height:17px;margin-bottom:18px}
.contact-row svg{width:20px;height:20px;flex:none}
.map{left:575px;top:3191px;width:253px;height:154px;background:linear-gradient(135deg,#e8ecef,#cfd8d2 55%,#b9d1e6)}
.newsletter{display:flex;height:36px}
.newsletter .field{width:148px;border:1px solid #555;font-size:12px;padding:10px 8px;color:var(--ink)}
.newsletter .go{width:82px;background:#6d6d72;color:var(--white);font-weight:700;font-size:13px;display:flex;align-items:center;justify-content:center}
.bottom{left:0;top:3398px;width:1164px;height:32px;background:var(--navy);color:var(--white);font-size:11px;display:flex;align-items:center;padding-left:14px;font-weight:600}
</style>
</head>
<body>
<div class="page">

  <header class="abs header">
    <div class="abs brand"><span class="dot"></span>Pathways Above Numbers Guild</div>
    <div class="abs topbar">
      <span class="item"><svg width="14" height="10" viewBox="0 0 14 10"><rect x="0.5" y="0.5" width="13" height="9" fill="none" stroke="#fff"/><path d="M1 1l6 5 6-5" fill="none" stroke="#fff"/></svg>info@panguild.com</span>
      <span class="item"><svg width="12" height="12" viewBox="0 0 24 24"><path d="M6 2l4 5-2 3a12 12 0 006 6l3-2 5 4-3 4C9 22 2 15 2 5z" fill="#fff"/></svg>800-555-0142</span>
      <span class="social"><i></i><i></i><i></i><i></i></span>
    </div>
    <nav class="abs nav">
      <a class="active"><svg viewBox="0 0 16 16"><path d="M1 8l7-6 7 6h-2v6H9v-4H7v4H3V8z" fill="#1f7fc1"/></svg>Home</a>
      <a><svg viewBox="0 0 16 16"><rect x="3" y="2" width="10" height="13" fill="#8e8c8a"/><rect x="5" y="4" width="2" height="2" fill="#fff"/><rect x="9" y="4" width="2" height="2" fill="#fff"/><rect x="5" y="8" width="2" height="2" fill="#fff"/><rect x="9" y="8" width="2" height="2" fill="#fff"/></svg>Who We Are</a>
      <a><svg viewBox="0 0 16 16"><rect x="2" y="9" width="3" height="6" fill="#8e8c8a"/><rect x="7" y="5" width="3" height="10" fill="#8e8c8a"/><rect x="12" y="2" width="3" height="13" fill="#8e8c8a"/></svg>What We Do</a>
      <a><svg viewBox="0 0 16 16"><circle cx="8" cy="8" r="6" fill="none" stroke="#8e8c8a" stroke-width="2"/><circle cx="8" cy="8" r="2" fill="#8e8c8a"/></svg>Expertise</a>
      <a><svg viewBox="0 0 16 16"><path d="M2 10l8-8 4 4-8 8H2z" fill="#8e8c8a"/></svg>News</a>
      <a><svg viewBox="0 0 24 24"><path d="M6 2l4 5-2 3a12 12 0 006 6l3-2 5 4-3 4C9 22 2 15 2 5z" fill="#8e8c8a"/></svg>Contact</a>
    </nav>
  </header>

  <section class="abs hero" role="img" aria-label="Hands touching a glowing digital bar chart interface">
    <div class="abs slider-dots"><i></i><i></i><i></i></div>
  </section>

  <section class="abs intro">
    <div class="abs lead">
      <div class="l1">Pathways Above Numbers Guild</div>
      <div class="l2">is the leading business analytics and</div>
      <div class="l3">Marketing Analytics Company</div>
    </div>
    <p class="abs">We provide marketing, consumer and business insights through the use of market research, business analytics and marketing analytics. We are a collection of several individuals each with specific expertise and come together to provide the best possible insights about their consumers/guests/customers.</p>
  </section>

  <section class="who">
    <h2 class="abs title"><span>Who <span class="acc">We Are</span></span></h2>
    <p style="top:1030px">Lorem ipsum dolor sit amet, consectetuer adipiscing elit, sed diam nonummy nibh euismod tincidunt ut laoreet dolore magna aliquam erat volutpat. Ut wisi enim ad minim veniam, quis nostrud exerci tation ullamcorper suscipit lobortis nisl ut aliquip ex ea commodo consequat.</p>
    <p style="top:1090px">Duis autem vel eum iriure dolor in hendrerit in vulputate velit esse molestie consequat, vel illum dolore eu feugiat nulla facilisis at vero eros et accumsan et iusto odio dignissim qui blandit praesent luptatum zzril delenit augue duis dolore te feugait nulla facilisi. Nam liber tempor cum soluta nobis eleifend option congue nihil imperdiet doming id quod mazim placerat facer possim assum.</p>
    <div class="btn">More About Us</div>
  </section>

  <section class="abs what" role="img" aria-label="Business papers with charts under a purple overlay">
    <h2 class="abs title">What We Do</h2>
    <p class="abs sub">We provide marketing, consumer and business insights through the use of market research, business analytics and marketing analytics.</p>
    <svg class="abs ring" width="1164" height="639" viewBox="0 0 1164 639">
      <path d="M150 340 A170 170 0 0 1 450 250" fill="none" stroke="#d6d6de" stroke-opacity=".55" stroke-width="46"/>
      <path d="M450 380 A170 170 0 0 0 760 380" fill="none" stroke="#d6d6de" stroke-opacity=".55" stroke-width="46"/>
      <path d="M760 250 A170 170 0 0 1 1060 340" fill="none" stroke="#d6d6de" stroke-opacity=".55" stroke-width="46"/>
    </svg>
    <div class="abs svc" style="left:173px;top:201px">
      <svg viewBox="0 0 64 64"><path d="M8 26h10l26-14v40L18 38H8z" fill="#1c1a4f"/><path d="M14 38l4 14h6l-3-14z" fill="#1c1a4f"/><path d="M50 24l8-4M50 32h9M50 40l8 4" stroke="#1f7fc1" stroke-width="3"/></svg>
      <p>Lorem ipsum dolor sit amet, consectetuer adipiscing elit, sed diam nonummy nibh euismod tincidunt ut laoreet dolore magna.</p>
    </div>
    <div class="abs svc" style="left:481px;top:201px">
      <svg viewBox="0 0 64 64"><circle cx="22" cy="9" r="6" fill="#1c1a4f"/><path d="M16 18h12l4 16-4 2v22h-6V38h-4v20h-4z" fill="#1c1a4f"/><path d="M34 30h26l-4 16H38z" fill="#1f7fc1"/><circle cx="42" cy="52" r="3" fill="#1c1a4f"/><circle cx="54" cy="52" r="3" fill="#1c1a4f"/></svg>
      <p>Lorem ipsum dolor sit amet, consectetuer adipiscing elit, sed diam nonummy nibh euismod tincidunt ut laoreet dolore magna.</p>
    </div>
    <div class="abs svc" style="left:792px;top:201px">
      <svg viewBox="0 0 64 64"><text x="4" y="30" font-family="Montserrat,sans-serif" font-size="28" font-weight="700" fill="#1c1a4f">$</text><rect x="6" y="40" width="8" height="18" fill="#1c1a4f"/><rect x="20" y="34" width="8" height="24" fill="#1c1a4f"/><rect x="34" y="26" width="8" height="32" fill="#1f7fc1"/><rect x="48" y="16" width="8" height="42" fill="#1f7fc1"/><path d="M42 12l10-8 8 8" fill="none" stroke="#1f7fc1" stroke-width="3"/></svg>
      <p>Lorem ipsum dolor sit amet, consectetuer adipiscing elit, sed diam nonummy nibh euismod tincidunt ut laoreet dolore magna.</p>
    </div>
    <div class="btn">Learn More</div>
  </section>

  <section class="abs expertise" role="img" aria-label="Business team meeting in a bright office">
    <h2 class="abs title"><span>Our <span class="acc">Expertise</span></span></h2>
  </section>
  <svg class="abs" style="left:360px;top:2020px" width="484" height="400" viewBox="0 0 484 400">
    <circle cx="242" cy="198" r="184" fill="none" stroke="#1c1a4f" stroke-width="4"/>
    <circle cx="242" cy="208" r="150" fill="#2c2a66"/>
    <g stroke="#fff" stroke-width="5" fill="#1c1a4f">
      <circle cx="242" cy="72" r="50"/><circle cx="60" cy="268" r="50"/><circle cx="424" cy="268" r="50"/>
    </g>
    <path d="M222 90V54M222 90h40M226 84l10-14 8 8 14-18" fill="none" stroke="#fff" stroke-width="3"/>
    <rect x="41" y="250" width="38" height="36" rx="4" fill="none" stroke="#fff" stroke-width="3"/><circle cx="60" cy="268" r="9" fill="none" stroke="#fff" stroke-width="3"/>
    <rect x="405" y="252" width="38" height="28" fill="none" stroke="#fff" stroke-width="3"/><path d="M424 280v10M415 268l6-6 6 4 8-8" fill="none" stroke="#fff" stroke-width="3"/>
  </svg>
  <div class="core"><div class="brand">PAN Guild</div></div>
  <div class="abs exp-text" style="left:250px;top:2036px;width:288px;padding-right:0"><h4>Business Analytics</h4><span style="display:block;width:240px">Lorem ipsum dolor sit amet, consectetuer adipiscing elit, sed diam nonummy nibh euismod tincidunt ut laoreet magna aliquam erat volutpat. Ut enim ad minim veniam.</span></div>
  <div class="abs exp-text" style="left:110px;top:2236px"><h4>Market Research</h4>Lorem ipsum dolor sit amet, consectetuer adipiscing elit, sed diam nonummy nibh euismod tincidunt ut laoreet magna aliquam erat volutpat. Ut enim ad minim veniam.</div>
  <div class="abs exp-text" style="left:844px;top:2236px"><h4>Marketing Analytics</h4>Lorem ipsum dolor sit amet, consectetuer adipiscing elit, sed diam nonummy nibh euismod tincidunt ut laoreet magna aliquam erat volutpat. Ut enim ad minim veniam.</div>

  <section class="abs news">
    <h2 class="abs title">Latest News</h2>
    <article class="abs card" style="left:85px;top:132px">
      <div class="photo" role="img" aria-label="Businessman at an office copier" style="background:linear-gradient(135deg,#dfe6ee,#9fb3c8 60%,#5d6f86)"></div>
      <h4>News #1<br>June 4, 2017</h4>
      <p>Lorem ipsum dolor sit amet, consectetuer adipiscing elit, sed diam nonummy nibh euis mod tincidunt ut laoreet dolore magna ali quam erat volutpat.</p>
    </article>
    <article class="abs card" style="left:423px;top:132px">
      <div class="photo" role="img" aria-label="City street with office towers at dusk" style="background:linear-gradient(180deg,#1b3a74,#2e5aa0 50%,#b8a16a 85%,#39404d)"></div>
      <h4>News #2<br>June 4, 2017</h4>
      <p>Lorem ipsum dolor sit amet, consectetuer adipiscing elit, sed diam nonummy nibh euis mod tincidunt ut laoreet dolore magna ali quam erat volutpat.</p>
    </article>
    <article class="abs card" style="left:759px;top:132px">
      <div class="photo" role="img" aria-label="Businessman facing a wall of sketched business diagrams" style="background:linear-gradient(135deg,#5a6d86,#9aabbf 50%,#3c4a60)"></div>
      <h4>News #3<br>June 4, 2017</h4>
      <p>Lorem ipsum dolor sit amet, consectetuer adipiscing elit, sed diam nonummy nibh euis mod tincidunt ut laoreet dolore magna ali quam erat volutpat.</p>
    </article>
  </section>

  <footer class="footer">
    <div class="abs foot-tab"></div>
    <div class="abs brand"><span class="dot"></span>Pathways Above Numbers Guild</div>

    <div class="abs col" style="left:51px">
      <h4 style="width:120px">Quick Links</h4>
      <ul><li>Home</li><li>Who We Are</li><li>What We Do</li><li>Expertise</li><li>News</li><li>Contact</li></ul>
    </div>
    <div class="abs col" style="left:228px">
      <h4 style="width:250px">Contact</h4>
      <div class="contact-row"><svg viewBox="0 0 20 20"><circle cx="10" cy="10" r="9" fill="none" stroke="#2b2b3a" stroke-width="1.5"/><path d="M10 4a4 4 0 00-4 4c0 3 4 8 4 8s4-5 4-8a4 4 0 00-4-4z" fill="#2b2b3a"/></svg><span><b>Pathways Above Numbers Guild</b><br>123 Lorem Ipsum St<br>Coral Bay, FL 33100</span></div>
      <div class="contact-row"><svg viewBox="0 0 20 20"><circle cx="10" cy="10" r="9" fill="none" stroke="#2b2b3a" stroke-width="1.5"/><path d="M7 5l2 3-1 1.5a6 6 0 003 3L12.5 11l3 2-1.5 2C9 15 5 11 5 6z" fill="#2b2b3a"/></svg><span>800-555-0142</span></div>
      <div class="contact-row"><svg viewBox="0 0 20 20"><circle cx="10" cy="10" r="9" fill="none" stroke="#2b2b3a" stroke-width="1.5"/><rect x="5.5" y="7" width="9" height="6" fill="none" stroke="#2b2b3a"/><path d="M5.5 7l4.5 3.5L14.5 7" fill="none" stroke="#2b2b3a"/></svg><span>info@panguild.com</span></div>
    </div>
    <div class="abs col" style="left:557px"><h4 style="width:271px">Find Us</h4></div>
    <div class="abs map" role="img" aria-label="Street map showing the office location"></div>
    <div class="abs col" style="left:886px">
      <h4 style="width:230px">Newsletter</h4>
      <div class="newsletter"><div class="field">Enter Email Address</div><div class="go">SIGN UP</div></div>
    </div>

    <div class="abs bottom">COPYRIGHT © 2017 PATHWAYS ABOVE NUMBERS GUILD. ALL RIGHTS RESERVED.<span class="social"><i></i><i></i><i></i><i></i></span></div>
  </footer>

</div>
</body>
</html>
```